Brindova Electrical Solutions needs a website

We need a new website designed because our current one is outdated. I would like a one-page website. We are a B2B company and want to maintain a professional appearance to appeal to project managers and directors.

for some reference, these are a few of my competitor's websites; we offer the same services.

https://valtrawire.com.au/services
https://www.drumwell.com.au/mechanical-electrical-services/
https://www.qulan.com.au/

Industry/Entity Type

Electrical

Number of Pages Required

1 page

Font styles to use
Sans Serif

Colors
0054AA
0677BA
7BADD7
CADEEF
E8F1F8

```html
<!DOCTYPE html>
<html lang="en">
<head>
<meta charset="utf-8">
<title>Brindova Electrical Solutions</title>
<link href="https://fonts.googleapis.com/css2?family=Montserrat:wght@600;700;800&family=Poppins:wght@400;500;600&display=swap" rel="stylesheet">
<style>
:root{
  --blue-deep:#0054AA;
  --blue:#0677BA;
  --blue-mid:#7BADD7;
  --blue-pale:#CADEEF;
  --blue-mist:#E8F1F8;
  --ink:#1b1b1b;
  --text:#3b3b3b;
  --dark:#211f20;
  --dark-line:#4a4849;
  --white:#ffffff;
  --footer:#1f1d1e;
}
*{box-sizing:border-box;margin:0;padding:0}
html,body{width:1200px;height:3649px;overflow:hidden}
body{position:relative;font-family:"Poppins",sans-serif;color:var(--text);background:var(--white)}
.abs{position:absolute}
h1,h2,h3,.display{font-family:"Montserrat",sans-serif;font-weight:800;color:var(--ink)}
a{color:inherit;text-decoration:none}

/* hero */
.hero{position:absolute;left:0;top:0;width:1200px;height:681px;overflow:hidden}
.hero-photo{position:absolute;inset:0;background:linear-gradient(100deg,#0c2a47 0%,#0f3a62 40%,#1c5687 65%,#2a6fa3 80%,#173f66 100%)}
.hero-shade{position:absolute;inset:0;background:linear-gradient(90deg,rgba(4,20,40,.55) 0%,rgba(4,20,40,.2) 60%,rgba(0,0,0,0) 100%)}
.brand{position:absolute;left:89px;top:22px;display:flex;align-items:center;gap:10px;color:var(--white);font-family:"Montserrat",sans-serif;font-weight:700;font-size:17px;letter-spacing:.5px}
.brand-dot{width:32px;height:32px;border-radius:50%;background:var(--white)}
.brand small{display:block;font-size:8px;letter-spacing:1.3px;font-weight:700}
.nav{position:absolute;top:33px;left:521px;display:flex;gap:24px;font-size:14px;font-weight:500;color:var(--white)}
.btn{display:inline-flex;align-items:center;justify-content:center;font-family:"Poppins",sans-serif;font-weight:600;font-size:12.5px;text-transform:uppercase;letter-spacing:.2px}
.btn-start{position:absolute;left:956px;top:18px;width:155px;height:49px;background:var(--white);color:var(--ink)}
.hero h1{position:absolute;left:88px;top:226px;width:640px;font-size:50px;line-height:55px;color:var(--white)}
.hero-lead{position:absolute;left:88px;top:402px;width:600px;font-size:15.5px;line-height:23px;color:var(--white)}
.btn-dark{position:absolute;left:88px;top:465px;width:169px;height:48px;background:var(--ink);color:var(--white)}
.btn-outline{position:absolute;left:269px;top:465px;width:132px;height:48px;border:1.5px solid var(--white);color:var(--white)}
.slide-count{position:absolute;left:1009px;top:583px;color:var(--white);font-family:"Montserrat",sans-serif;font-weight:800;font-size:46px;line-height:1}
.slide-count span{font-size:27px}

/* why */
.section-title{position:absolute;left:0;width:1200px;text-align:center;font-size:37px}
.section-sub{position:absolute;left:0;width:1200px;text-align:center;font-size:14px;color:var(--text)}
.why-line{position:absolute;left:153px;top:965px;width:893px;border-top:1.5px dashed #8a8a8a}
.why-dot{position:absolute;top:960px;width:11px;height:11px;border-radius:50%;background:var(--blue)}
.why-card{position:absolute;top:850px;width:160px;height:230px;background:var(--white);box-shadow:0 8px 28px rgba(0,0,0,.09);text-align:center}
.why-card svg.icon{position:absolute;left:50px;top:30px}
.why-card .stem{position:absolute;left:79px;top:115px;height:22px;border-left:1.5px dashed #8a8a8a}
.why-card .node{position:absolute;left:73px;top:136px;width:14px;height:14px;border-radius:50%;border:1.5px dashed #8a8a8a}
.why-card p{position:absolute;left:0;top:168px;width:160px;font-family:"Montserrat",sans-serif;font-weight:700;font-size:14px;line-height:18px;color:var(--ink)}

/* who */
.services{position:absolute;left:0;top:1610px;width:1200px;height:532px;background:var(--dark)}
.who-photo{position:absolute;left:179px;top:1170px;width:393px;height:516px;background:linear-gradient(160deg,#2b2b35 0%,#6d6f80 35%,#c9c6d6 50%,#555766 70%,#1e1c22 100%)}
.who h2{position:absolute;left:638px;top:1265px;font-size:37px}
.who p{position:absolute;left:638px;top:1327px;width:410px;font-size:13.5px;line-height:22.3px}
.btn-blue{position:absolute;background:linear-gradient(90deg,var(--blue-deep),var(--blue));color:var(--white)}
.who .btn-blue{left:638px;top:1498px;width:136px;height:48px}

/* services */
.services h2{position:absolute;left:89px;top:135px;font-size:37px;color:var(--white)}
.services .btn-blue{left:975px;top:136px;width:136px;height:48px}
.svc-rule{position:absolute;left:71px;top:348px;width:1058px;border-top:1px solid var(--dark-line)}
.svc-vr{position:absolute;border-left:1px solid var(--dark-line)}
.svc{position:absolute;display:flex;align-items:center;gap:12px;color:var(--white);font-family:"Montserrat",sans-serif;font-weight:700;font-size:14px;line-height:18px}
.svc svg{flex:none}
.svc-active{position:absolute;left:601px;top:211px;width:255px;height:137px;background:linear-gradient(135deg,var(--blue-deep),var(--blue))}
.svc-active .badge{position:absolute;left:22px;top:-31px;width:61px;height:59px;background:var(--white);display:flex;align-items:center;justify-content:center}
.svc-active h3{position:absolute;left:22px;top:41px;font-size:14px;line-height:18px;color:var(--white);font-weight:700}
.svc-active p{position:absolute;left:22px;top:88px;width:210px;font-size:10.5px;line-height:17px;color:var(--white)}

/* projects */
.proj{position:absolute;top:2301px;width:329px;height:367px;overflow:visible}
.proj .photo{position:absolute;inset:0}
.proj .veil{position:absolute;inset:0;background:linear-gradient(180deg,rgba(0,0,0,0) 50%,rgba(0,0,0,.7) 100%)}
.proj h3{position:absolute;left:27px;top:275px;font-size:19px;color:var(--white)}
.proj p{position:absolute;left:27px;top:305px;width:280px;font-size:11.5px;line-height:18px;color:var(--white)}
.proj .go{position:absolute;left:261px;top:349px;width:38px;height:38px;background:linear-gradient(135deg,var(--blue-deep),var(--blue));display:flex;align-items:center;justify-content:center}
.view-all{position:absolute;left:0;top:2714px;width:1200px;text-align:center;font-size:12.5px;font-weight:600;color:var(--ink)}
.view-all span{border-bottom:1.5px solid var(--ink);padding-bottom:2px}

/* testimonials */
.testi{position:absolute;left:0;top:2784px;width:592px;height:478px;background:linear-gradient(90deg,#eaeaec,#f3f3f5)}
.testi-photo{position:absolute;left:592px;top:2784px;width:608px;height:478px;background:linear-gradient(200deg,#1f3a57 0%,#4a6682 40%,#b7a58b 70%,#e9dcc3 100%)}
.testi h2{position:absolute;left:108px;top:76px;font-size:37px}
.stars{position:absolute;left:108px;top:138px;display:flex;gap:5px}
.testi .quote{position:absolute;left:108px;top:178px;width:430px;font-size:14px;line-height:22.3px}
.testi .quote p+p{margin-top:8px}
.person{position:absolute;left:108px;top:358px;display:flex;align-items:center;gap:12px}
.avatar{width:42px;height:42px;border-radius:50%;background:var(--blue-pale)}
.person b{display:block;font-family:"Montserrat",sans-serif;font-weight:700;font-size:14px;color:var(--blue-deep);line-height:17px}
.person span{font-size:13px;color:#666}
.arrows{position:absolute;left:108px;top:419px;display:flex;gap:16px;align-items:center}

/* footer */
.footer{position:absolute;left:0;top:3262px;width:1200px;height:387px;background:var(--footer);color:var(--white)}
.fcol{position:absolute;top:84px}
.fcol h4{font-family:"Montserrat",sans-serif;font-weight:600;font-size:17px;margin-bottom:18px}
.fcol li{list-style:none;font-size:12.5px;line-height:27px}
.contact-item{display:flex;gap:9px;margin-bottom:15px;font-size:12.5px;line-height:17px}
.contact-item b{display:block;font-weight:600;font-size:11.5px}
.subscribe{display:flex;align-items:center;justify-content:space-between;margin-top:12px;width:274px;height:50px;background:#2d2b2c;padding:0 18px;font-size:12px;color:#bbb}
.f-rule{position:absolute;left:84px;top:332px;width:1062px;border-top:1px solid #3a3839}
.copyright{position:absolute;left:0;top:348px;width:1200px;text-align:center;font-size:16px}
.to-top{position:absolute;left:1125px;top:309px;width:48px;height:48px;background:linear-gradient(135deg,var(--blue-deep),var(--blue));display:flex;align-items:center;justify-content:center}
</style>
</head>
<body>

<header class="hero">
  <div class="hero-photo" role="img" aria-label="Electrician in hard hat and safety glasses testing a switchboard"></div>
  <div class="hero-shade"></div>
  <div class="brand"><span class="brand-dot"></span><div>BRINDOVA<small>ELECTRICAL SOLUTIONS</small></div></div>
  <nav class="nav"><a>Home</a><a>About Us</a><a>Services</a><a>Project</a><a>Testimonials</a></nav>
  <a class="btn btn-start">Get Strated</a>
  <h1>Professional Mechanical, Electrical, and HVAC Solutions</h1>
  <p class="hero-lead">Delivering innovative, efficient, and reliable solutions for commercial and industrial projects across Australia.</p>
  <a class="btn btn-dark">Explore Services</a>
  <a class="btn btn-outline">Contact Us</a>
  <div class="slide-count">01/<span>03</span></div>
</header>

<section class="why">
  <h2 class="section-title" style="top:748px">Why Choose Us</h2>
  <p class="section-sub" style="top:800px">Why Project Managers and Directors Choose Us</p>
  <div class="why-line"></div>
  <span class="why-dot" style="left:148px"></span>
  <span class="why-dot" style="left:1041px"></span>
  <div class="why-card" style="left:215px">
    <svg class="icon" width="60" height="60" viewBox="0 0 60 60" fill="none" stroke="#0677BA" stroke-width="2"><circle cx="30" cy="30" r="14"/><circle cx="30" cy="30" r="9"/><path d="M25 30l4 4 6-7"/><path d="M22 44l-4 12 6-3 4 5 2-10M38 44l4 12-6-3-4 5-2-10"/><path d="M30 3l2 4 4 .5-3 3 1 4-4-2-4 2 1-4-3-3 4-.5z"/></svg>
    <span class="stem"></span><span class="node"></span><p>Proven<br>Expertise</p>
  </div>
  <div class="why-card" style="left:419px">
    <svg class="icon" width="60" height="60" viewBox="0 0 60 60" fill="none" stroke="#0677BA" stroke-width="2"><path d="M20 8h10v6a4 4 0 108 0V8h8v12h-6a4 4 0 100 8h6v12H36v-6a4 4 0 10-8 0v6H20V28h-6a4 4 0 110-8h6z"/><path d="M24 40v14M36 40v14"/></svg>
    <span class="stem"></span><span class="node"></span><p>End-to-End<br>Solutions</p>
  </div>
  <div class="why-card" style="left:622px">
    <svg class="icon" width="60" height="60" viewBox="0 0 60 60" fill="none" stroke="#0677BA" stroke-width="2"><circle cx="30" cy="16" r="10"/><path d="M25 16l4 4 6-7"/><path d="M4 38l10-8 8 2 8 6 8-6 8-2 10 8M16 42l8 8 6-4 6 4 8-8"/></svg>
    <span class="stem"></span><span class="node"></span><p>Reliable<br>Partner</p>
  </div>
  <div class="why-card" style="left:826px">
    <svg class="icon" width="60" height="60" viewBox="0 0 60 60" fill="none" stroke="#0677BA" stroke-width="2"><path d="M30 8a10 10 0 00-6 18v6h12v-6a10 10 0 00-6-18z"/><path d="M26 36h8M27 40h6"/><path d="M12 40h8l4 6h12l4-6h8v10H12z"/><path d="M30 2v3M18 8l2 2M42 8l-2 2"/></svg>
    <span class="stem"></span><span class="node"></span><p>Sustainable<br>Solutions</p>
  </div>
</section>

<section class="services">
  <h2>Our Services</h2>
  <a class="btn btn-blue">Learn More</a>
  <span class="svc-vr" style="left:346px;top:211px;height:275px"></span>
  <span class="svc-vr" style="left:601px;top:211px;height:275px"></span>
  <span class="svc-vr" style="left:856px;top:211px;height:275px"></span>
  <div class="svc-rule"></div>

  <div class="svc" style="left:122px;top:253px"><svg width="54" height="54" viewBox="0 0 54 54" fill="none" stroke="#fff" stroke-width="1.8"><rect x="4" y="30" width="14" height="20"/><rect x="22" y="6" width="26" height="18"/><circle cx="34" cy="40" r="8"/><circle cx="34" cy="40" r="3"/><path d="M8 36h6M8 42h6M27 12l6 6 10-8"/></svg>Mechanical<br>Electrical Service</div>
  <div class="svc" style="left:385px;top:253px"><svg width="54" height="54" viewBox="0 0 54 54" fill="none" stroke="#fff" stroke-width="1.8"><circle cx="27" cy="27" r="9"/><circle cx="27" cy="27" r="3"/><path d="M27 14v-4M27 44v-4M14 27h-4M44 27h-4M18 18l-3-3M39 39l-3-3M36 18l3-3M15 39l3-3"/><circle cx="27" cy="27" r="22" stroke-dasharray="3 5"/></svg>BMCS &amp; HVAC</div>
  <div class="svc-active">
    <div class="badge"><svg width="34" height="34" viewBox="0 0 34 34" fill="none" stroke="#211f20" stroke-width="1.6"><rect x="8" y="4" width="16" height="26"/><path d="M12 9h8M12 14h8M12 19h8M4 30h26M24 14h5v16"/></svg></div>
    <h3>Commercial &amp;<br>Industrial Projects</h3>
    <p>Tailored solutions for large-scale industrial and commercial...</p>
  </div>
  <div class="svc" style="left:890px;top:253px"><svg width="54" height="54" viewBox="0 0 54 54" fill="none" stroke="#fff" stroke-width="1.8"><path d="M24 8a12 12 0 00-7 22v6h14v-6a12 12 0 00-7-22z"/><circle cx="38" cy="38" r="8"/><circle cx="38" cy="38" r="3"/><path d="M38 26v4M38 46v4M26 38h4M46 38h4"/></svg>Project Design</div>

  <div class="svc" style="left:122px;top:393px"><svg width="54" height="54" viewBox="0 0 54 54" fill="none" stroke="#fff" stroke-width="1.8"><circle cx="20" cy="18" r="8"/><path d="M6 48v-6a14 14 0 0128 0v6"/><circle cx="40" cy="16" r="7"/><circle cx="40" cy="16" r="2.5"/><path d="M40 6v3M40 23v3M30 16h3M47 16h3"/></svg>Project<br>Management</div>
  <div class="svc" style="left:385px;top:393px"><svg width="54" height="54" viewBox="0 0 54 54" fill="none" stroke="#fff" stroke-width="1.8"><circle cx="27" cy="30" r="16"/><circle cx="27" cy="30" r="7"/><path d="M14 18h26v-4H14zM22 14V8h10v6M27 4v4M27 46v4M11 30H6M48 30h-5"/></svg>Engineering</div>
  <div class="svc" style="left:632px;top:393px"><svg width="54" height="54" viewBox="0 0 54 54" fill="none" stroke="#fff" stroke-width="1.8"><circle cx="36" cy="16" r="10"/><path d="M32 20l8-8M32 13h1M39 19h1"/><path d="M4 38l10-6h12l4 4H18M4 48l8-4h16l16-12-4-4-12 8"/></svg>Commissioning</div>
  <div class="svc" style="left:890px;top:393px"><svg width="54" height="54" viewBox="0 0 54 54" fill="none" stroke="#fff" stroke-width="1.8"><rect x="4" y="4" width="20" height="22"/><rect x="28" y="4" width="22" height="22"/><rect x="4" y="30" width="20" height="20"/><rect x="28" y="30" width="22" height="20"/><path d="M10 10h8v10h-8zM33 12h4M41 12h4M33 19h4M41 19h4M10 36v8M14 36v8M18 36v8M34 36h10v8H34z"/></svg>Switchboard<br>Design &amp; Installation</div>
</section>

<section class="who">
  <div class="who-photo" role="img" aria-label="Steel truss bridge lit at night with traffic light trails"></div>
  <h2>Who We Are</h2>
  <p>At [Your Company Name], we specialize in delivering tailored mechanical, electrical, and HVAC solutions. With years of experience and a commitment to excellence, we partner with businesses to bring projects to life efficiently and professionally. From design to commissioning, we’re trusted by project managers and directors across Australia.”</p>
  <a class="btn btn-blue">Read More</a>
</section>

<section class="projects">
  <h2 class="section-title" style="top:2204px">Proven Success in Action</h2>
  <p class="section-sub" style="top:2258px">Take a look at some of our recent projects that highlight our capabilities and commitment to excellence.</p>
  <article class="proj" style="left:89px">
    <div class="photo" role="img" aria-label="Close-up of high-voltage insulators and switchgear" style="background:linear-gradient(160deg,#cfd1d1,#8b8e8f 50%,#3f4142)"></div>
    <div class="veil"></div>
    <h3>ABC Commercial Building</h3>
    <p>Full electrical fit-out, BMCS integration, and HVAC system installation.</p>
    <span class="go"><svg width="10" height="12" viewBox="0 0 10 12" fill="none" stroke="#fff" stroke-width="1.8"><path d="M3 2l4 4-4 4"/></svg></span>
  </article>
  <article class="proj" style="left:435px">
    <div class="photo" role="img" aria-label="Industrial factory floor with robotic machinery" style="background:linear-gradient(170deg,#d9dadb,#8c8f93 45%,#6a5a52 75%,#3c3c3e)"></div>
    <div class="veil"></div>
    <h3>XYZ Industrial Facility</h3>
    <p>Switchboard design, mechanical electrical services, and project commissioning.</p>
    <span class="go"><svg width="10" height="12" viewBox="0 0 10 12" fill="none" stroke="#fff" stroke-width="1.8"><path d="M3 2l4 4-4 4"/></svg></span>
  </article>
  <article class="proj" style="left:782px">
    <div class="photo" role="img" aria-label="Technician working at a control desk in a dim plant room" style="background:linear-gradient(160deg,#b58a5e,#6f4f35 45%,#2f2a26)"></div>
    <div class="veil"></div>
    <h3>Sydney Corporate Office</h3>
    <p>Comprehensive HVAC installation and BMCS optimization.</p>
    <span class="go"><svg width="10" height="12" viewBox="0 0 10 12" fill="none" stroke="#fff" stroke-width="1.8"><path d="M3 2l4 4-4 4"/></svg></span>
  </article>
  <a class="view-all"><span>VIEW ALL PROJECT</span></a>
</section>

<section class="testi">
  <h2>Testimonials</h2>
  <div class="stars">
    <svg width="20" height="19" viewBox="0 0 20 19"><path fill="#0677BA" d="M10 0l3 6.5 7 .7-5.3 4.7 1.6 7L10 15.3 3.7 19l1.6-7L0 7.2l7-.7z"/></svg>
    <svg width="20" height="19" viewBox="0 0 20 19"><path fill="#0677BA" d="M10 0l3 6.5 7 .7-5.3 4.7 1.6 7L10 15.3 3.7 19l1.6-7L0 7.2l7-.7z"/></svg>
    <svg width="20" height="19" viewBox="0 0 20 19"><path fill="#0677BA" d="M10 0l3 6.5 7 .7-5.3 4.7 1.6 7L10 15.3 3.7 19l1.6-7L0 7.2l7-.7z"/></svg>
    <svg width="20" height="19" viewBox="0 0 20 19"><path fill="#0677BA" d="M10 0l3 6.5 7 .7-5.3 4.7 1.6 7L10 15.3 3.7 19l1.6-7L0 7.2l7-.7z"/></svg>
    <svg width="20" height="19" viewBox="0 0 20 19"><path fill="#0677BA" d="M10 0l3 6.5 7 .7-5.3 4.7 1.6 7L10 15.3 3.7 19l1.6-7L0 7.2l7-.7z"/></svg>
  </div>
  <div class="quote">
    <p>It is a long established fact that a reader will be distracted by the readable content of a page when looking at its layout. The point of using Lorem Ipsum is that it has a more-or-less normal distribution of letters,</p>
    <p>There are many variations of passages of Lorem Ipsum available, but the majority have suffered alteration in some form, by injected humour, or randomised.</p>
  </div>
  <div class="person"><span class="avatar" role="img" aria-label="Client portrait"></span><div><b>Marcus T.</b><span>Project Manager</span></div></div>
  <div class="arrows">
    <svg width="20" height="12" viewBox="0 0 20 12" fill="none" stroke="#1b1b1b" stroke-width="1.6"><path d="M19 6H2M7 1L2 6l5 5"/></svg>
    <svg width="34" height="18" viewBox="0 0 34 18" fill="none" stroke="#0677BA" stroke-width="2"><path d="M1 9h30M24 2l7 7-7 7"/></svg>
  </div>
</section>
<div class="testi-photo" role="img" aria-label="Steel transmission tower against a bright sunset sky"></div>

<footer class="footer">
  <div class="fcol" style="left:135px"><h4>Quick Links</h4><ul><li>Home</li><li>About Us</li><li>Services</li><li>Project</li><li>Testimonials</li></ul></div>
  <div class="fcol" style="left:330px"><h4>Information</h4><ul><li>Privacy Policy</li><li>Disclaimer</li><li>Terms &amp; Condition</li><li>Site Map</li></ul></div>
  <div class="fcol" style="left:521px"><h4>Contact Us</h4>
    <div class="contact-item"><svg width="13" height="13" viewBox="0 0 24 24"><path fill="#fff" d="M6.6 10.8a15 15 0 006.6 6.6l2.2-2.2a1 1 0 011-.3 11 11 0 003.6.6 1 1 0 011 1V20a1 1 0 01-1 1A17 17 0 013 4a1 1 0 011-1h3.5a1 1 0 011 1 11 11 0 00.6 3.6 1 1 0 01-.3 1z"/></svg><div><b>PHONE</b>02 8011 4270</div></div>
    <div class="contact-item"><svg width="13" height="13" viewBox="0 0 24 24"><path fill="#fff" d="M2 5h20v14H2zm2 2v.5l8 5 8-5V7z"/></svg><div><b>EMAIL</b>info@brindovasolutions.com.au</div></div>
    <div class="contact-item" style="margin-top:24px"><svg width="13" height="14" viewBox="0 0 24 24"><path fill="#fff" d="M12 2a7 7 0 00-7 7c0 5 7 13 7 13s7-8 7-13a7 7 0 00-7-7zm0 9.5A2.5 2.5 0 1112 6a2.5 2.5 0 010 5.5z"/></svg><div><b>ADDRESS</b>Sydney NSW, Australia</div></div>
  </div>
  <div class="fcol" style="left:791px"><h4>Newsletter</h4>
    <p style="font-size:12px">Subscribe to our newsletter</p>
    <div class="subscribe"><span>Enter email address</span><svg width="16" height="16" viewBox="0 0 24 24"><path fill="#fff" d="M2 11l20-9-7 20-3-8z"/></svg></div>
  </div>
  <div class="f-rule"></div>
  <p class="copyright">© Copyright 2024. All rights reserved.</p>
  <span class="to-top"><svg width="12" height="8" viewBox="0 0 12 8" fill="none" stroke="#fff" stroke-width="1.8"><path d="M1 7l5-5 5 5"/></svg></span>
</footer>

</body>
</html>
```